Say goodbye to Paper Cuts - Modern B2B Paper Ad

We need a design for a full page magazine ad

Company Overview:
FileNimbus is an administration support company for Northern Lending Insider. We are running a full page ad in Northern Lending Insider magazine

Ad Copy
"Say Goodbye to Paper Cuts"
"On-Demand Admin Support for Mortgage Professionals"
[website url at the bottom]

Ad Dimensions:
Trim: (w) 8.25” x (h) 10.875”
Bleed: (w) 8.75” x (h) 11.375”
Type: (w) 7.5” x (h) 10.125”

Ad Requirements (provided by the magazine)
Please supply all artwork in PC format only, either in EPS, Tiff or PDF format with the following requirements:

- All files must be 300 dpi high resolution with CMYK process colour.
- Any Pantone colours that are found will automatically be converted to CMYK. Please double check that all colours are in CMYK.
- EPS files must be in outline path for all fonts and embedded images.
- Tiff files must be in PC format, flatten with no layer.
- PDF files must be press optimized and embedded with images and fonts.
- All Double page ads and Full page ads must be in press-optimized PDF files.
- 0.125" bleed with crop marks are required for Double page ads, Full page ads and Panel ads to be supplied on artwork where specified.
- Ad files in Microsoft Word, Excel, PowerPoint or other software are NOT acceptable.
- Materials received should be in a printable file with no conversion required.

Industry/Entity Type

It Company

Font styles to use
Sans Serif

Requirements
Must have
• Bold, clean style

```html
<!DOCTYPE html>
<html lang="en">
<head>
<meta charset="utf-8">
<title>FileNimbus – Say Goodbye to Paper Cuts</title>
<link href="https://fonts.googleapis.com/css2?family=Montserrat:wght@200;300;500;700&display=swap" rel="stylesheet">
<style>
  :root {
    --backdrop: #d6d7d9;
    --page: #ffffff;
    --brand-blue: #2d5eb0;
    --brand-navy: #1e3a78;
    --band-light: #f1f2f4;
    --band-dark: #cfd3d9;
    --ink: #1f2a44;
    --photo-light: #f7f5f3;
    --photo-mid: #e8e1dc;
    --photo-warm: #e7c3b6;
  }
  * { margin: 0; padding: 0; box-sizing: border-box; }
  html, body {
    width: 1200px;
    height: 768px;
    overflow: hidden;
    background: var(--backdrop);
    font-family: "Montserrat", sans-serif;
  }
  .ad-page {
    position: absolute;
    left: 308px;
    top: 0;
    width: 584px;
    height: 768px;
    background: var(--page);
    overflow: hidden;
  }
  .brand-mark {
    position: absolute;
    display: flex;
    align-items: center;
    gap: 6px;
    color: var(--brand-navy);
    font-weight: 700;
  }
  .brand-mark .brand-square {
    background: var(--brand-navy);
  }
  .brand-mark--top {
    left: 34px;
    top: 34px;
    font-size: 13px;
  }
  .brand-mark--top .brand-square { width: 10px; height: 10px; }
  .hero-photo {
    position: absolute;
    left: 150px;
    top: 110px;
    width: 434px;
    height: 470px;
    background:
      radial-gradient(ellipse at 45% 60%, var(--photo-warm) 0%, rgba(231,195,182,0) 55%),
      linear-gradient(160deg, var(--photo-light) 0%, var(--photo-mid) 100%);
  }
  .shapes {
    position: absolute;
    left: 0;
    top: 0;
  }
  .headline {
    position: absolute;
    left: 26px;
    top: 510px;
    color: #ffffff;
    line-height: 1;
  }
  .headline .say {
    display: block;
    font-size: 20px;
    font-weight: 300;
    padding-left: 18px;
  }
  .headline .goodbye {
    display: block;
    font-size: 40px;
    font-weight: 200;
    letter-spacing: 0.5px;
    margin-top: 2px;
  }
  .headline .tail {
    display: block;
    font-size: 15px;
    font-weight: 300;
    padding-left: 40px;
    margin-top: 4px;
  }
  .signoff {
    position: absolute;
    right: 34px;
    top: 640px;
    text-align: right;
  }
  .brand-mark--bottom {
    position: static;
    justify-content: flex-end;
    font-size: 30px;
  }
  .brand-mark--bottom .brand-square { width: 22px; height: 22px; }
  .tagline {
    margin-top: 4px;
    color: var(--ink);
    font-size: 14px;
    font-weight: 500;
    line-height: 1.25;
  }
  .tagline strong { font-weight: 700; }
  .site-url {
    display: inline-block;
    margin-top: 10px;
    padding: 6px 22px;
    background: var(--brand-blue);
    color: #ffffff;
    font-size: 15px;
    font-weight: 500;
    letter-spacing: 0.5px;
  }
</style>
</head>
<body>
  <main class="ad-page">
    <div class="brand-mark brand-mark--top">
      <span class="brand-square"></span>
      <span class="brand-name">FileNimbus</span>
    </div>

    <div class="hero-photo" role="img" aria-label="Photo of a stressed office worker carrying a tall stack of overflowing red and black binders"></div>

    <svg class="shapes" width="584" height="768" viewBox="0 0 584 768" aria-hidden="true">
      <defs>
        <linearGradient id="swoosh-blue" x1="0" y1="0" x2="1" y2="1">
          <stop offset="0" stop-color="#3a6cc0"/>
          <stop offset="1" stop-color="#1f4c9a"/>
        </linearGradient>
        <linearGradient id="band-grey" x1="0" y1="0" x2="1" y2="0">
          <stop offset="0" stop-color="#f4f5f7"/>
          <stop offset="1" stop-color="#cfd3d9"/>
        </linearGradient>
      </defs>
      <path class="swoosh" d="M0 480 C120 500 250 560 360 640 L0 660 Z" fill="url(#swoosh-blue)"/>
      <path class="bottom-band" d="M0 650 C180 620 400 600 584 560 L584 768 L0 768 Z" fill="url(#band-grey)"/>
    </svg>

    <h1 class="headline">
      <span class="say">Say</span>
      <span class="goodbye">Goodbye</span>
      <span class="tail">to Paper Cuts</span>
    </h1>

    <div class="signoff">
      <div class="brand-mark brand-mark--bottom">
        <span class="brand-square"></span>
        <span class="brand-name">FileNimbus</span>
      </div>
      <p class="tagline">On-Demand Admin Support for<br><strong>Mortgage Professionals</strong></p>
      <span class="site-url">www.filenimbus.ca</span>
    </div>
  </main>
</body>
</html>
```